Distribution/Printing company needs a web site to inform prospective customers on what we do.

Distribution/Printing/Packaging company needs a web site to inform prospective customers on what we do. Please look at our direct to consumer web site (under development) for an idea of the product lines we sell: storedev.thebrindlestock.com
Logo files are attached as is a flyer that is under development which contains other information about the company (this is to be used for content- not to be posted as is). The web site should be focused on our business customer base and is not intended to be direct to consumer. Site should have a link to our consumer web site.
Site design should be mobile friendly, or mobile could be redirected to a mobile version. This web site will be strictly informational and will not be designed for any sales transactions.

Target Market(s)

Manufacturing and retail businesses, any other multi-site business that would benefit from centralized pricing and budget controls we can provide (banks, medical/dental offices, educational facilities, etc).

Requirements
Must have
• 1) Top level menu: Products, about us, locations, contact us, news
• 2) page with news/promotions that is easily updated
• 3) "contact us" form (name, company, phone, email address) email link
• 4) link to www.store.thebrindlestock.com with information that lower pricing is available for businesses
• 5) SEO keywords
• 6) Link to powerpoint presentation file
Nice to have
• 1) our phone number should appear on every page near the top

```html
<!DOCTYPE html>
<html lang="en">
<head>
<meta charset="utf-8">
<title>Harbor Crest Supply — Packaging, Printing, Distribution</title>
<link rel="stylesheet" href="https://fonts.googleapis.com/css2?family=Open+Sans:wght@400;600;700&display=swap">
<style>
:root{
  --orange:#f26b3a;
  --dark:#2f323b;
  --darker:#24262d;
  --ink:#333333;
  --muted:#6b6b6b;
  --line:#e3e3e3;
  --white:#ffffff;
  --chip:#5a5d66;
}
*{box-sizing:border-box;margin:0;padding:0}
html,body{width:753px;height:1200px;overflow:hidden;background:var(--white)}
body{font-family:"Open Sans",Arial,sans-serif;color:var(--ink);position:relative;font-size:8px}
.abs{position:absolute}

/* top bar */
.topbar{left:0;top:0;width:753px;height:27px;background:var(--dark);color:#d8d8d8;font-size:7.5px}
.topbar .email{left:100px;top:8px;display:flex;align-items:center;gap:5px}
.topbar .store-link{left:555px;top:0;width:97px;height:27px;background:var(--darker);display:flex;align-items:center;justify-content:center;gap:5px}

/* header */
.brand{left:100px;top:37px}
.brand-mark{width:12px;height:12px;background:#1e1e1e}
.brand-name{font-weight:700;font-size:12px;letter-spacing:.3px;color:#1e1e1e;margin-top:2px}
.brand-tag{font-size:7.5px;font-weight:600;color:#1e1e1e}
.connect{left:356px;top:42px;display:flex;align-items:center;gap:12px;font-size:8px;font-weight:700}
.connect .dot{width:6px;height:6px;border-radius:50%;background:#555}
.search{left:531px;top:38px;width:121px;height:18px;border:1px solid var(--line);font-size:7px;color:#aaa;padding:4px 6px}
.quote{left:396px;top:68px;display:flex;gap:8px;align-items:center}
.callus{left:574px;top:68px;display:flex;gap:8px;align-items:center}
.small-cap{font-size:6px;color:#999;letter-spacing:.3px}
.orange-big{color:var(--orange);font-size:10.5px}

/* nav */
.nav{left:0;top:107px;width:753px;height:27px;border-top:1px solid var(--line);border-bottom:1px solid var(--line)}
.nav ul{list-style:none;display:flex;position:absolute;left:100px;top:0}
.nav li{font-size:7.5px;font-weight:600;text-transform:uppercase;padding:8px 0;margin-right:24px;color:#444}
.nav li.active{color:var(--orange);border-bottom:2px solid var(--orange)}

/* hero */
.hero{left:0;top:134px;width:753px;height:233px;background:linear-gradient(90deg,#f4f4f4,#e6e6e6)}
.hero-photo{left:100px;top:0;width:220px;height:233px;background:linear-gradient(180deg,#d9d5cf 0%,#c49a63 55%,#a97d4a 100%)}
.hero-kicker{left:335px;top:30px;font-size:17px;color:var(--orange);letter-spacing:.3px}
.hero-title{left:336px;top:62px;width:281px;height:38px;background:var(--orange);color:var(--white);font-size:25px;font-weight:700;text-align:center;line-height:38px}
.hero-copy{left:335px;top:111px;width:285px;font-size:8.4px;line-height:14px;color:#555}
.btn-dark{left:335px;top:184px;width:79px;height:24px;background:var(--dark);color:var(--white);font-size:7.5px;font-weight:600;text-align:center;line-height:24px;border-radius:2px}

/* services */
.service{top:396px;width:170px;text-align:center}
.service .icon{width:50px;height:50px;border-radius:50%;background:#ececec;margin:0 auto;display:flex;align-items:center;justify-content:center}
.service h3{font-size:8px;font-weight:700;margin-top:17px;text-transform:uppercase}
.service p{font-size:7px;line-height:11px;color:#555;margin-top:6px}
.service a{display:inline-block;margin-top:8px;font-size:6.5px;color:var(--orange);text-decoration:underline}
.divider{left:100px;top:547px;width:552px;height:2px;background:#eaeaea}

/* section headers */
.section-head{left:100px;width:552px;height:27px;border:1px solid var(--line);font-size:7.5px;font-weight:700;padding:0 12px;line-height:26px;text-transform:uppercase}
.arrows{position:absolute;right:8px;top:6px;display:flex;gap:3px}
.arrows span{width:14px;height:14px;background:#d9d9d9;display:flex;align-items:center;justify-content:center}

/* categories */
.cat{top:610px;width:100px;height:98px;border:1px solid var(--line)}
.cat .pic{position:absolute;left:6px;top:6px;width:86px;height:62px}
.cat .rule{position:absolute;left:6px;top:73px;width:86px;height:2px;background:var(--orange)}
.cat .label{position:absolute;left:0;top:81px;width:100%;text-align:center;font-size:6.5px;text-transform:uppercase}

/* featured products (informational) */
.prod{top:780px;width:130px;height:224px;border:1px solid var(--line)}
.prod .pic{position:absolute;left:15px;top:12px;width:98px;height:125px;background:linear-gradient(180deg,#f2f2f2,#dcdcdc)}
.prod .rule{position:absolute;left:6px;top:162px;width:116px;height:2px;background:var(--orange)}
.prod .name{position:absolute;left:10px;top:170px;font-size:6.5px;font-weight:600;text-transform:uppercase}
.prod .more{position:absolute;left:10px;top:192px;font-size:6.5px;color:var(--orange);text-decoration:underline}

/* footer */
.footer{left:0;top:1028px;width:753px;height:147px;background:var(--dark);color:#c9c9c9}
.footer h4{font-size:11px;color:var(--white);font-weight:600;text-transform:uppercase;letter-spacing:.3px}
.foot-nav{left:100px;top:11px}
.foot-nav ul{list-style:none;margin-top:6px}
.foot-nav li{font-size:7.5px;line-height:13px}
.foot-about{left:304px;top:11px;width:156px}
.foot-about p{font-size:7.5px;line-height:12px;margin-top:6px;text-align:justify}
.foot-contact{left:495px;top:11px}
.foot-contact p{font-size:7.5px;line-height:13px;margin-top:6px}
.social{display:flex;gap:6px;margin-top:15px}
.social span{width:24px;height:24px;background:#1f2127;display:flex;align-items:center;justify-content:center}
.social i{width:7px;height:7px;border-radius:50%;background:#cfcfcf;display:block}
.vline{top:15px;width:1px;height:120px;background:#41444d}
.bottombar{left:0;top:1175px;width:753px;height:25px;background:var(--darker);color:#c9c9c9;font-size:6.5px}
.pay{top:6px;display:flex;gap:6px;left:100px}
.pay span{width:24px;height:13px;border-radius:2px;background:var(--chip)}
.copy{right:101px;top:8px}
</style>
</head>
<body>

<div class="abs topbar">
  <div class="abs email">
    <svg width="9" height="7" viewBox="0 0 9 7"><rect x=".5" y=".5" width="8" height="6" fill="none" stroke="#d8d8d8"/><path d="M.5 .5 4.5 4 8.5 .5" fill="none" stroke="#d8d8d8"/></svg>
    <span>Email: info@harborcrestsupply.com</span>
  </div>
  <div class="abs store-link"><span>CONSUMER STORE »</span></div>
</div>

<div class="abs brand">
  <div class="brand-mark"></div>
  <div class="brand-name">HARBOR CREST SUPPLY</div>
  <div class="brand-tag">Packaging • Printing • Distribution</div>
</div>
<div class="abs connect">
  <span>Connect with us!</span>
  <span class="dot"></span><span class="dot"></span><span class="dot"></span><span class="dot"></span>
</div>
<div class="abs search">Search</div>
<div class="abs quote">
  <svg width="18" height="13" viewBox="0 0 18 13"><rect x=".5" y=".5" width="17" height="12" fill="none" stroke="#bbb"/><path d="M.5 .5 9 7 17.5 .5" fill="none" stroke="#bbb"/></svg>
  <div><div class="small-cap">WANT AN APPROXIMATE PRICE?</div><div class="orange-big">GET A FREE QUOTE »</div></div>
</div>
<div class="abs callus">
  <svg width="14" height="16" viewBox="0 0 14 16"><path d="M3 1 5.5 4 4 6c1 2 2.5 3.8 4.5 5l2-1.5L13 12l-2 3C6 14 1 8 1 3z" fill="none" stroke="#bbb"/></svg>
  <div><div class="small-cap">CALL US NOW!</div><div class="orange-big">715.555.0142</div></div>
</div>

<nav class="abs nav">
  <ul>
    <li class="active">Home</li><li>About</li><li>Products</li><li>Packaging</li>
    <li>Office Supplies</li><li>Locations</li><li>Contact Us</li><li>News</li>
  </ul>
</nav>

<section class="abs hero">
  <div class="abs hero-photo" role="img" aria-label="Delivery worker in a green shirt carrying a cardboard box"></div>
  <div class="abs hero-kicker">MEETING ALL OF YOUR</div>
  <div class="abs hero-title">PACKAGING NEEDS</div>
  <p class="abs hero-copy">Lorem ipsum dolor sit amet conse ctetur adipisicing elit, sed do eiusmod tempor incididunt ut labore et dolore magna aliqua. Ut enim ad minim veniam, quis nostrud exercitation ullamco laboris nisi ut aliquip ex ea commodo consequat. Duis aute irure dolor in reprehende.</p>
  <div class="abs btn-dark">READ MORE</div>
</section>

<div class="abs service" style="left:102px">
  <div class="icon"><svg width="20" height="18" viewBox="0 0 20 18"><path d="M10 1 1 6h18z" fill="var(--orange)"/><rect x="3" y="7" width="2.5" height="7" fill="var(--orange)"/><rect x="8.7" y="7" width="2.5" height="7" fill="var(--orange)"/><rect x="14.5" y="7" width="2.5" height="7" fill="var(--orange)"/><rect x="1" y="15" width="18" height="2.5" fill="var(--orange)"/></svg></div>
  <h3>Banks Move</h3>
  <p>Neque porro quisquam est qui tdolorem<br>ipsum quia dolor sit amet, consectetur</p>
  <a>READ MORE</a>
</div>
<div class="abs service" style="left:291px">
  <div class="icon"><svg width="16" height="20" viewBox="0 0 16 20"><rect x="1" y="2" width="14" height="18" fill="var(--orange)"/><rect x="6.8" y="6" width="2.4" height="7" fill="#fff"/><rect x="4.5" y="8.3" width="7" height="2.4" fill="#fff"/><rect x="6" y="15" width="4" height="5" fill="#fff"/></svg></div>
  <h3>Hospital Move</h3>
  <p>Neque porro quisquam est qui tdolorem<br>ipsum quia dolor sit amet, consectetur</p>
  <a>READ MORE</a>
</div>
<div class="abs service" style="left:480px">
  <div class="icon"><svg width="20" height="20" viewBox="0 0 20 20"><path d="M10 2 3 8h14z" fill="var(--orange)"/><rect x="4" y="8" width="12" height="11" fill="var(--orange)"/><rect x="8" y="13" width="4" height="6" fill="#fff"/><circle cx="10" cy="10" r="1.6" fill="#fff"/></svg></div>
  <h3>School Move</h3>
  <p>Neque porro quisquam est qui tdolorem<br>ipsum quia dolor sit amet, consectetur</p>
  <a>READ MORE</a>
</div>
<div class="abs divider"></div>

<div class="abs section-head" style="top:571px">Browse Categories
  <div class="arrows"><span><svg width="5" height="6"><path d="M4 0 1 3l3 3" fill="none" stroke="#666"/></svg></span><span><svg width="5" height="6"><path d="M1 0l3 3-3 3" fill="none" stroke="#666"/></svg></span></div>
</div>
<div class="abs cat" style="left:100px"><div class="pic" role="img" aria-label="Stack of cardboard boxes" style="background:linear-gradient(180deg,#e7c58c,#c8914c)"></div><div class="rule"></div><div class="label">Packaging</div></div>
<div class="abs cat" style="left:213px"><div class="pic" role="img" aria-label="Calculator and office supplies" style="background:linear-gradient(180deg,#d8d8d8,#8a8a8a)"></div><div class="rule"></div><div class="label">Office</div></div>
<div class="abs cat" style="left:326px"><div class="pic" role="img" aria-label="Colored storage bins" style="background:linear-gradient(90deg,#d6453a,#3d6fc2,#e7c23b)"></div><div class="rule"></div><div class="label">Storage</div></div>
<div class="abs cat" style="left:439px"><div class="pic" role="img" aria-label="Light bulbs" style="background:linear-gradient(180deg,#f2f2f2,#c9c9c9)"></div><div class="rule"></div><div class="label">Retail</div></div>
<div class="abs cat" style="left:552px"><div class="pic" role="img" aria-label="Safety and industrial equipment" style="background:linear-gradient(180deg,#e9a23b,#c5392f)"></div><div class="rule"></div><div class="label">Industrial</div></div>

<div class="abs section-head" style="top:743px">Featured Products
  <div class="arrows"><span><svg width="5" height="6"><path d="M4 0 1 3l3 3" fill="none" stroke="#666"/></svg></span><span><svg width="5" height="6"><path d="M1 0l3 3-3 3" fill="none" stroke="#666"/></svg></span></div>
</div>
<div class="abs prod" style="left:100px"><div class="pic" role="img" aria-label="Three-step folding stool ladder"></div><div class="rule"></div><div class="name">Ladder 3-Step Stool White</div><a class="more">READ MORE</a></div>
<div class="abs prod" style="left:241px"><div class="pic" role="img" aria-label="Three-step folding stool ladder"></div><div class="rule"></div><div class="name">Ladder 3-Step Stool White</div><a class="more">READ MORE</a></div>
<div class="abs prod" style="left:381px"><div class="pic" role="img" aria-label="Three-step folding stool ladder"></div><div class="rule"></div><div class="name">Ladder 3-Step Stool White</div><a class="more">READ MORE</a></div>
<div class="abs prod" style="left:522px"><div class="pic" role="img" aria-label="Three-step folding stool ladder"></div><div class="rule"></div><div class="name">Ladder 3-Step Stool White</div><a class="more">READ MORE</a></div>

<footer class="abs footer">
  <div class="abs foot-nav">
    <h4>Navigate</h4>
    <ul><li>Home</li><li>About</li><li>Products</li><li>Packaging</li><li>Office Supplies</li><li>Locations</li><li>Contact us</li><li>News</li></ul>
  </div>
  <div class="abs vline" style="left:285px"></div>
  <div class="abs foot-about">
    <h4>About Us</h4>
    <p>Lorem ipsum dolor sit amet, onsectetur adipisicing elit, sed do eiusmod tempor incididunt ut labore et dolore magna aliqua. Ut enim ad minim veniam, quis nostrud exercitation ullamco laboris nisi ut aliquip ex ea commodo consequat. Etiam diam augue, aliquam vitae aliquet et, sagittis non orci.</p>
  </div>
  <div class="abs vline" style="left:472px"></div>
  <div class="abs foot-contact">
    <h4>Contact Us</h4>
    <p>Phone: + (848) 555 440 110<br>Fax: + (212) 555 60 60 34<br>Email: info@harborcrestsupply.com<br>Adress: 1248P, Larkspur Ave New York</p>
    <div class="social"><span><i></i></span><span><i></i></span><span><i></i></span><span><i></i></span></div>
  </div>
</footer>
<div class="abs bottombar">
  <div class="abs pay"><span></span><span></span><span></span><span></span></div>
  <div class="abs copy">© 2015 Harbor Crest Supply. All Rights Reserved.</div>
</div>

</body>
</html>
```